Veranaxis Business Card and Letter Head

We are a leadership assessment consultancy based in Sydney, Australia. We help executive-level decison-makers select leaders for more senior level roles in corporate and government organisations. Our methodology is based on the latest research from the field of neuroscience.
We need a business card design and matching letter head that presents our company, Veranaxis, as a:
1. trusted adviser to senior executive-level decison makers
2. niche consultancy who are experts in the field of assessing leadership talent
3. results-focused solution provider who balance scientific methods with pragmatic solutions
The following company details should be used in all designs:
Company Name: Veranaxis
Details (for business card):
Daniel Prescott
Senior Talent Adviser
Level 17, Brenning Tower
7 Brenning Square
Sydney, NSW 2011 Australia
Phone: 1300 482 716
Mobile: 0412 573 208
Email: daniel.prescott@veranaxis.com.au
Website: veranaxis.com.au
I have attached the logo for Veranaxis (for both a white and black background) - your business card and letter head designs must incoporate this logo and colour scheme.
Thanks for your interest in this project, I'm looking forward to receiving your ideas.
Regards,
Daniel
Executive-level decison-makers in corporate and government organisations (e.g., CEO, VP, Head of Human Resources)
Leadership

```html
<!DOCTYPE html>
<html lang="en">
<head>
<meta charset="utf-8">
<title>Veranaxis Stationery</title>
<link rel="stylesheet" href="https://fonts.googleapis.com/css2?family=Cabin:wght@400;600&family=Raleway:wght@700&display=swap">
<style>
  :root {
    --paper: #ffffff;
    --charcoal: #3b3b3b;
    --charcoal-deep: #2f2f2f;
    --brand-red: #c0311f;
    --ink-grey: #5a5a5a;
    --logo-grey: #4a4a4a;
    --rule: #111111;
  }
  * { margin: 0; padding: 0; box-sizing: border-box; }
  html, body { width: 848px; height: 1200px; overflow: hidden; background: var(--paper); }
  .sheet { position: relative; width: 848px; height: 1200px; font-family: "Cabin", "Gill Sans", sans-serif; }
  .block { position: absolute; }
  .tab-dark { left: 20px; top: 52px; width: 124px; height: 45px; background: var(--charcoal); }
  .address-panel {
    left: 162px; top: 52px; width: 282px; height: 141px; background: var(--brand-red);
    color: #fff; font-size: 11px; line-height: 13.7px; padding: 10px 0 0 15px; font-style: normal;
  }
  .address-panel p + p { margin-top: 13.7px; }
  .band-dark { left: 455px; top: 147px; width: 371px; height: 46px; background: var(--charcoal); }
  .wordmark { display: flex; align-items: center; gap: 8px; font-family: "Raleway", sans-serif; font-weight: 700; letter-spacing: -0.5px; }
  .wordmark .mark-square { width: 0.7em; height: 0.7em; background: var(--brand-red); }
  .letter-logo { position: absolute; left: 542px; top: 70px; font-size: 32px; color: var(--logo-grey); }

  .card { position: absolute; width: 364px; height: 202px; border: 1.5px solid var(--rule); overflow: hidden; }
  .card-front { left: 396px; top: 672px; background: var(--paper); }
  .card-front .strip { position: absolute; left: 0; top: 0; width: 19px; height: 100%; background: var(--charcoal); }
  .card-front .strip-foot { position: absolute; left: 0; top: 118px; width: 53px; height: 84px; background: var(--charcoal); }
  .card-logo { position: absolute; left: 40px; top: 22px; font-size: 28px; color: var(--logo-grey); }
  .card-name { position: absolute; left: 40px; top: 73px; font-size: 13.5px; color: var(--brand-red); }
  .card-contacts { position: absolute; left: 140px; top: 112px; font-size: 10.5px; line-height: 13.8px; color: var(--ink-grey); list-style: none; }
  .card-contacts li { display: flex; align-items: flex-start; gap: 4px; }
  .card-contacts svg { width: 10px; height: 10px; margin-top: 2px; flex: none; fill: var(--ink-grey); }
  .card-contacts .pair { gap: 14px; }
  .card-contacts .pair span { display: flex; gap: 4px; }

  .card-back { left: 397px; top: 905px; background: var(--charcoal); }
  .back-plate { position: absolute; left: 0; top: 102px; width: 212px; height: 78px; background: var(--charcoal-deep); }
  .back-logo { position: absolute; left: 18px; top: 22px; font-size: 28px; color: #f2f2f2; }
  .back-logo .mark-square { background: #f2f2f2; }
</style>
</head>
<body>
<main class="sheet">
  <section class="letterhead" aria-label="Letterhead">
    <div class="block tab-dark"></div>
    <address class="block address-panel">
      <p>Level 17, Brenning Tower<br>7 Brenning Square<br>Sydney, NSW 2011 Australia</p>
      <p>Phone: 1300 482 716<br>Mobile: 0412 573 208<br>Email: daniel.prescott@veranaxis.com.au<br>Website: veranaxis.com.au</p>
    </address>
    <div class="wordmark letter-logo"><span class="mark-square"></span>Veranaxis</div>
    <div class="block band-dark"></div>
  </section>

  <section class="card card-front" aria-label="Business card front">
    <div class="strip"></div>
    <div class="strip-foot"></div>
    <div class="wordmark card-logo"><span class="mark-square"></span>Veranaxis</div>
    <p class="card-name">Daniel Prescott - Senior Talent Adviser</p>
    <ul class="card-contacts">
      <li class="pair">
        <span><svg viewBox="0 0 10 10"><path d="M1 4c0-2 2-3 4-3s4 1 4 3L7 5 6 3H4L3 5z M2 6h6v3H2z"/></svg>1300 482 716</span>
        <span><svg viewBox="0 0 10 10"><rect x="3" y="0.5" width="4" height="9" rx="1"/></svg>0412 573 208</span>
      </li>
      <li><svg viewBox="0 0 10 10"><circle cx="5" cy="5" r="4" fill="none" stroke="#5a5a5a" stroke-width="1.2"/><circle cx="5" cy="5" r="1.6"/></svg>daniel.prescott@veranaxis.com.au</li>
      <li><svg viewBox="0 0 10 10"><rect x="0.5" y="1.5" width="9" height="7" fill="none" stroke="#5a5a5a"/><rect x="0.5" y="1.5" width="9" height="2"/></svg>veranaxis.com.au</li>
      <li><svg viewBox="0 0 10 10"><path d="M5 0.5 0.5 5H2v4.5h2.3V6.5h1.4v3H8V5h1.5z"/></svg>Level 17, Brenning Tower 7 Brenning Square<br>Sydney, NSW 2011 Australia</li>
    </ul>
  </section>

  <section class="card card-back" aria-label="Business card back">
    <div class="back-plate">
      <div class="wordmark back-logo"><span class="mark-square"></span>Veranaxis</div>
    </div>
  </section>
</main>
</body>
</html>
```